Professional Business Card for Luxury Hotel & Resort Development Firm. Advisory firm

Project Overview: We are a specialized advisory firm focused on Hotel & Resort Development. Our clients are high-net-worth investors and major hospitality brands.

Design Requirements:

Style: Minimalist, sophisticated, and trustworthy. We want to avoid looking too "corporate" or "dry"—it should feel premium.

Key Elements: Please incorporate our logo [もしロゴがあれば] and emphasize a clean layout with plenty of white space.

Color Palette: We prefer Grey and White or Black and White to evoke a sense of luxury and stability.

Typography: Professional garamond, or sans-serif or elegant serif fonts

Goal: The card should feel substantial and high-end when handed to a client, reflecting our expertise in multi-million dollar developments.

I am currently on a business trip for field research and have limited access to my desktop. Additionally, I have just provided detailed technical feedback to a designer and am waiting for their refined proposals. To ensure the final logo meets the high standards of my new advisory firm, I would like to extend the deadline by 7 days. Thank you for your support.

Target Market(s)

High-net-worth investors, luxury hospitality brands, and real estate developers.

Contact Information for Business Card

Firm Name: Corvale Advisory Group, My Name: Kenshiro Fujisawa, Title: Founder, Address 5-8-4 Kitahoshino Midori Yokohama Japan 226-0071, email address: kfujisawa@corvaleadvisoryx.com, Tel: +81 80-4217-3058. Front Site (Primary): Japanese translation of the back side, Please use a clean Japanese font (like Mincho) that complements the Garmond on the English side Back side: English. Note for Japanese text: since the frond side is the main fae, please ensure the layout is clean and professional. Please use a high-quality Mincho ( Serif-style) font for Japanese to mach the Garmond used on the English side. Text for Front side (Japanese) Corvale Advisory Group, 役職:代表、藤沢謙志郎、226-0071 横浜市緑区北星野5-8-4. Name of the firm can stay in English.

Other font styles liked:
• Font Preference: Please use Garamond for all text to maintain a consistent, elegant, and classic professional look.

Requirements
Must have
• Professional and clean layout, high-end feel.
Nice to have
• Minimalist design with subtle luxury accents.

```html
<!DOCTYPE html>
<html lang="en">
<head>
<meta charset="utf-8">
<title>Corvale Advisory Group — Business Card</title>
<link rel="stylesheet" href="https://fonts.googleapis.com/css2?family=EB+Garamond:wght@400;500;600&family=Shippori+Mincho:wght@400;500&display=swap">
<style>
  :root {
    --backdrop: #222224;
    --card: #2a292e;
    --ink-light: #ececec;
    --ink-grey: #8a8a8c;
    --accent-grey: #6f6f72;
    --faint: #333238;
  }
  * { box-sizing: border-box; margin: 0; padding: 0; }
  html, body {
    width: 1200px; height: 800px; overflow: hidden;
    background: var(--backdrop);
    font-family: "EB Garamond", Garamond, serif;
  }
  .canvas { position: relative; width: 1200px; height: 800px; }
  .card {
    position: absolute; width: 580px; height: 350px;
    background: var(--card);
    border-radius: 3px;
    overflow: hidden;
  }
  .card--front { left: 60px; top: 40px; }
  .card--back { left: 560px; top: 410px; }

  /* Front (Japanese) */
  .brand {
    display: flex; align-items: center; gap: 12px;
    color: var(--ink-grey);
  }
  .brand__mark { width: 22px; height: 22px; background: var(--accent-grey); flex: none; }
  .brand__name { font-size: 24px; font-weight: 500; letter-spacing: 0.06em; }
  .card--front .brand {
    position: absolute; left: 0; right: 0; top: 120px; justify-content: center;
  }
  .card--front .brand__name { font-size: 30px; }
  .front-details {
    position: absolute; left: 0; right: 0; bottom: 54px; text-align: center;
    font-family: "Shippori Mincho", serif;
    font-size: 15px; color: var(--ink-light); letter-spacing: 0.04em;
  }

  /* Back (English) */
  .card--back .brand { position: absolute; left: 36px; top: 40px; }
  .card--back .brand__name { font-size: 19px; }
  .brand-watermark {
    position: absolute; right: 26px; top: 60px; width: 250px;
    font-size: 40px; line-height: 1.05; font-weight: 500;
    color: var(--faint); text-align: right; letter-spacing: 0.03em;
  }
  .person {
    position: absolute; left: 36px; top: 150px;
    padding-left: 16px; border-left: 9px solid var(--accent-grey);
  }
  .person__name { font-size: 30px; font-weight: 500; color: var(--ink-grey); line-height: 1.05; letter-spacing: 0.02em; }
  .person__title { font-size: 15px; color: var(--ink-light); margin-top: 2px; }
  .contact-list { position: absolute; left: 70px; top: 244px; list-style: none; }
  .contact-list li {
    display: flex; align-items: center; gap: 12px;
    font-size: 15px; color: var(--ink-light); line-height: 26px;
  }
  .contact-list svg { width: 14px; height: 14px; flex: none; }
  .address {
    position: absolute; right: 36px; top: 220px; text-align: right;
    font-size: 14px; color: var(--ink-light); line-height: 1.35;
  }
</style>
</head>
<body>
<main class="canvas">

  <section class="card card--front" lang="ja" aria-label="Card front, Japanese">
    <div class="brand" lang="en">
      <span class="brand__mark"></span>
      <span class="brand__name">Corvale Advisory Group</span>
    </div>
    <p class="front-details">役職:代表、藤沢謙志郎、226-0071 横浜市緑区北星野5-8-4</p>
  </section>

  <section class="card card--back" aria-label="Card back, English">
    <div class="brand-watermark" aria-hidden="true">Corvale Advisory Group</div>
    <div class="brand">
      <span class="brand__mark"></span>
      <span class="brand__name">Corvale Advisory Group</span>
    </div>
    <div class="person">
      <h1 class="person__name">Kenshiro Fujisawa</h1>
      <p class="person__title">Founder</p>
    </div>
    <ul class="contact-list">
      <li>
        <svg viewBox="0 0 16 16" aria-hidden="true"><path fill="#8a8a8c" d="M3.6 1.5 6 4.2 4.8 5.9c.8 1.9 2.3 3.4 4.2 4.3l1.7-1.2 2.7 2.4-1.3 2.3C7 13.6 2.3 8.9 1.3 2.8z"/></svg>
        +81 80-4217-3058
      </li>
      <li>
        <svg viewBox="0 0 16 16" aria-hidden="true"><circle cx="8" cy="8" r="6.3" fill="none" stroke="#8a8a8c" stroke-width="1.4"/><path d="M1.7 8h12.6M8 1.7c-3 3.4-3 9.2 0 12.6M8 1.7c3 3.4 3 9.2 0 12.6" fill="none" stroke="#8a8a8c" stroke-width="1.1"/></svg>
        www.corvaleadvisoryx.com
      </li>
      <li>
        <svg viewBox="0 0 16 16" aria-hidden="true"><rect x="1.5" y="3.5" width="13" height="9" fill="none" stroke="#8a8a8c" stroke-width="1.4"/><path d="M1.5 3.8 8 9l6.5-5.2" fill="none" stroke="#8a8a8c" stroke-width="1.3"/></svg>
        kfujisawa@corvaleadvisoryx.com
      </li>
    </ul>
    <address class="address" style="font-style: normal;">
      5-8-4 Kitahoshino Midori<br>
      Yokohama Japan 226-0071
    </address>
  </section>

</main>
</body>
</html>
```